Concrete Construction page for marketing my business

I need a nice website where I can upload photos of current work, at the moment I am using linkwall but I would like to have my own webpage, I would need a nice and easy menu at the top of the page

you can find my linkwall page here https://www.linkwall.example/TarvenGroup

For images and ideas...

My Linkwall page is

www.linkwall.example/tarvengroupadelaide/

```html
<!DOCTYPE html>
<html lang="en">
<head>
<meta charset="utf-8">
<title>Tarven Group – Concrete Construction</title>
<link href="https://fonts.googleapis.com/css2?family=Montserrat:ital,wght@0,600;0,700;0,800;1,800;1,900&family=Open+Sans:wght@400;600;700&display=swap" rel="stylesheet">
<style>
:root{
  --blue:#1f3f9f;
  --blue-dark:#162e7a;
  --ink:#222;
  --grey-text:#555;
  --light:#f1f1f1;
  --footer:#2a2a2a;
  --footer-bottom:#1c1c1c;
  --white:#fff;
}
*{box-sizing:border-box;margin:0;padding:0}
html,body{width:1200px;height:4108px;overflow:hidden}
body{position:relative;font-family:"Open Sans",Arial,sans-serif;color:var(--ink);background:var(--white)}
.abs{position:absolute}
.heading{font-family:"Montserrat",Arial,sans-serif;font-style:italic;font-weight:900;font-size:46px;letter-spacing:1px;color:var(--ink)}
.heading span{color:var(--blue)}
.btn{display:inline-block;font-family:"Montserrat",Arial,sans-serif;font-weight:700;font-size:15px;border-radius:30px;padding:14px 30px;text-transform:uppercase}
.btn-blue{background:var(--blue);color:var(--white)}
.btn-outline{border:2px solid var(--blue);color:var(--blue);background:var(--white)}
.photo{overflow:hidden}
p.body{font-size:15px;line-height:1.7;color:var(--grey-text)}

/* header */
.topbar{left:880px;top:0;width:320px;height:38px;background:var(--blue);border-bottom-left-radius:24px;display:flex;align-items:center;padding-left:34px;padding-right:10px;gap:8px;color:var(--white);font-size:13px}
.topbar .dot{flex:none;width:24px;height:24px;border-radius:50%;background:var(--white);opacity:.9}
.topbar .mail{margin-right:auto}
.logo{left:112px;top:30px;font-family:"Montserrat",Arial,sans-serif;font-weight:800;font-size:30px;line-height:1.05;color:var(--blue)}
.logo .l2{display:block;padding-left:118px}
.nav{left:360px;top:68px;display:flex;gap:28px;font-family:"Montserrat",Arial,sans-serif;font-weight:700;font-size:15px}
.nav a{color:var(--ink);text-decoration:none}
.nav a.active{color:var(--blue);border-bottom:3px solid var(--blue);padding-bottom:6px}
.call{left:910px;top:60px;display:flex;align-items:center;gap:14px}
.call .ic{width:48px;height:48px;border-radius:50%;background:var(--blue);display:flex;align-items:center;justify-content:center}
.call small{display:block;font-size:12px;color:#888;font-weight:700}
.call strong{font-family:"Montserrat",Arial,sans-serif;font-size:22px;color:var(--blue)}

/* hero */
.hero{left:0;top:140px;width:1200px;height:680px}
.hero-photo{left:0;top:0;width:1200px;height:640px;background:linear-gradient(180deg,#c9c6c0 0%,#8c8a86 45%,#77777a 100%)}
.hero-card{left:612px;top:372px;width:540px;height:540px;border-radius:50%;background:var(--white);border:14px solid #e6e6e6;text-align:center;padding-top:70px;box-shadow:0 6px 20px rgba(0,0,0,.15)}
.hero-card .welcome{font-family:"Montserrat",Arial,sans-serif;font-weight:800;font-style:italic;color:var(--blue);font-size:24px;letter-spacing:1px}
.hero-card h1{font-family:"Montserrat",Arial,sans-serif;font-style:italic;font-weight:900;font-size:50px;color:var(--blue);line-height:1.05}
.hero-card p{font-size:22px;line-height:1.45;color:var(--ink);width:430px;margin:14px auto 24px}
.slider-dots{left:1138px;top:328px;display:flex;flex-direction:column;gap:12px}
.slider-dots i{width:16px;height:16px;border-radius:50%;border:2px solid var(--white);background:rgba(255,255,255,.4)}
.slider-dots i.on{background:var(--white)}

/* about */
.about-big{left:112px;top:862px;width:420px;height:420px;border-radius:50%;background:linear-gradient(135deg,#d8d3c9,#9b968c);border:8px solid var(--white);box-shadow:0 0 0 2px #ddd}
.about-small{left:370px;top:1092px;width:230px;height:230px;border-radius:50%;background:linear-gradient(160deg,#cfd6de,#7e838a);border:10px solid var(--white);box-shadow:0 4px 14px rgba(0,0,0,.2)}
.about-text{left:672px;top:880px;width:440px}
.about-text .heading{margin-bottom:30px}
.about-text p{margin-bottom:18px}

/* services */
.services{left:0;top:1408px;width:1200px;height:760px;background:var(--light)}
.services .heading{position:absolute;left:0;width:1200px;top:60px;text-align:center}
.svc{position:absolute;top:170px;width:300px;text-align:center}
.svc .pic{width:300px;height:300px;border-radius:50%;margin:0 auto;border:10px solid var(--white);box-shadow:0 3px 10px rgba(0,0,0,.15)}
.svc.mid .pic{border-color:var(--blue)}
.svc .icon{width:62px;height:62px;margin:-36px auto 0;position:relative;background:#9a9a9a;border-radius:8px;display:flex;align-items:center;justify-content:center}
.svc.mid .icon{background:var(--blue)}
.svc h3{font-family:"Montserrat",Arial,sans-serif;font-weight:700;font-size:18px;margin:22px 0 10px}
.svc p{font-size:15px;line-height:1.55;color:var(--grey-text);width:280px;margin:0 auto 24px}
.svc .btn{font-size:13px;padding:10px 24px}
.arrow{position:absolute;top:300px;width:36px;height:36px;border-radius:50%;display:flex;align-items:center;justify-content:center}

/* benefits */
.benefits{left:0;top:2172px;width:1200px;height:600px}
.benefits ul{position:absolute;left:112px;top:156px;width:480px;list-style:none;color:var(--white)}
.benefits li{font-size:14px;line-height:1.55;padding-left:28px;position:relative;margin-bottom:18px}
.benefits li::before{content:"";position:absolute;left:4px;top:8px;width:7px;height:7px;border-radius:50%;background:var(--white)}
.benefits .heading{position:absolute;left:112px;top:80px;color:var(--white)}
.benefits .actions{position:absolute;left:112px;top:476px;display:flex;gap:16px}
.btn-dark{background:#1b1b1b;color:var(--white)}
.btn-white{background:var(--white);color:var(--blue);text-transform:none;font-size:16px}
.benefit-photo{left:640px;top:2264px;width:448px;height:420px;border-radius:24px;border:8px solid var(--white);background:linear-gradient(160deg,#8fa77a 0%,#c9c6bf 45%,#a7a39b 100%);box-shadow:0 6px 20px rgba(0,0,0,.3)}

/* projects */
.projects-title{left:0;top:2880px;width:1200px;text-align:center}
.proj{border-radius:18px;border:4px solid #1e1e1e}
.proj.blue{border-color:var(--blue)}

/* footer */
.footer{left:0;top:3520px;width:1200px;height:588px}
.f-logo{left:112px;top:340px;font-family:"Montserrat",Arial,sans-serif;font-weight:800;font-size:28px;line-height:1.05;color:var(--white)}
.f-logo .l2{display:block;padding-left:118px}
.f-col{top:250px;color:var(--white)}
.f-col h4{font-family:"Montserrat",Arial,sans-serif;font-weight:800;font-size:18px;margin-bottom:24px}
.f-col ul{list-style:none}
.f-col li{font-size:14px;margin-bottom:20px;padding-left:34px;position:relative;color:#ddd}
.f-col li::before{content:"";position:absolute;left:0;top:2px;width:14px;height:14px;border-radius:50%;border:2px solid #ddd}
.contact-row{display:flex;gap:14px;margin-bottom:18px}
.contact-row .ic{flex:none;width:40px;height:40px;border-radius:50%;background:var(--white);display:flex;align-items:center;justify-content:center}
.contact-row b{display:block;font-size:14px}
.contact-row span{font-size:12px;color:#ccc}
.f-bottom{left:0;top:528px;width:1200px;height:60px;background:var(--footer-bottom);color:#ccc;font-size:13px;display:flex;align-items:center;justify-content:center}
.f-social{position:absolute;right:40px;top:16px;display:flex;gap:10px}
.f-social i{width:28px;height:28px;border-radius:4px;background:#3a3a3a}
.f-social i.on{background:var(--blue)}
</style>
</head>
<body>

<!-- Header -->
<div class="abs topbar"><span class="mail">hello@tarvengroup.example</span><span class="dot"></span><span class="dot"></span><span class="dot"></span></div>
<div class="abs logo">TARVEN<span class="l2">GROUP</span></div>
<nav class="abs nav"><a class="active" href="#">HOME</a><a href="#">ABOUT US</a><a href="#">SERVICES</a><a href="#">PROJECTS</a><a href="#">CONTACT US</a></nav>
<div class="abs call">
  <div class="ic"><svg width="22" height="22" viewBox="0 0 24 24"><path fill="#fff" d="M6.6 10.8a15.1 15.1 0 0 0 6.6 6.6l2.2-2.2c.3-.3.7-.4 1-.2 1.1.4 2.3.6 3.6.6.6 0 1 .4 1 1V20c0 .6-.4 1-1 1A17 17 0 0 1 3 4c0-.6.4-1 1-1h3.5c.6 0 1 .4 1 1 0 1.2.2 2.4.6 3.6.1.3 0 .7-.2 1z"/></svg></div>
  <div><small>CALL US</small><strong>+61 400 000 123</strong></div>
</div>

<!-- Hero -->
<section class="abs hero">
  <div class="abs photo hero-photo" role="img" aria-label="Photo of a new brick home with a freshly laid exposed aggregate concrete driveway"></div>
  <svg class="abs" style="left:0;top:440px" width="1200" height="240" viewBox="0 0 1200 240">
    <path d="M0 110 C300 230 700 240 1200 120 L1200 240 L0 240Z" fill="#fff"/>
    <path d="M0 110 C300 230 700 240 1200 120 L1200 150 C700 250 300 240 0 150Z" fill="#1f3f9f"/>
  </svg>
  <div class="abs slider-dots"><i class="on"></i><i></i><i></i></div>
</section>
<div class="abs hero-card">
  <div class="welcome">WELCOME TO</div>
  <h1>TARVEN GROUP</h1>
  <p>Lorem ipsum dolor sit amet, consectetur dos adipiscing elit, sed do eiusmod tempor it labore et sit amet dolorea.</p>
  <span class="btn btn-blue">Get Started</span>
</div>

<!-- About -->
<div class="abs about-big" role="img" aria-label="Close-up of an exposed aggregate concrete path"></div>
<div class="abs about-small" role="img" aria-label="Modern house with a concrete driveway"></div>
<div class="abs about-text">
  <h2 class="heading">ABOUT <span>US</span></h2>
  <p class="body">Lorem ipsum dolor sit amet, consectetur adipiscing elit, sed do eiusmod tempor incididunt ut labore et dolore magna aliqua. Ut enim ad minim veniam, quis nostrud exercitation ullamco laboris nisi ut aliquip ex ea commodo consequat. Duis aute irure dolor in reprehen.</p>
  <p class="body">Lorem ipsum dolor sit amet, consectetur adipiscing elit, sed do eiusmod tempor incididunt ut labore et dolore magna tempor incididunt aliqua.</p>
  <span class="btn btn-blue">Learn More</span>
</div>

<!-- Services -->
<section class="abs services">
  <h2 class="heading">OUR <span>SERVICES</span></h2>
  <div class="arrow" style="left:40px;background:#fff;box-shadow:0 1px 4px rgba(0,0,0,.2)"><svg width="14" height="14" viewBox="0 0 14 14"><path d="M9 2 4 7l5 5" stroke="#1f3f9f" stroke-width="2.5" fill="none"/></svg></div>
  <div class="arrow" style="left:1124px;background:#1f3f9f"><svg width="14" height="14" viewBox="0 0 14 14"><path d="m5 2 5 5-5 5" stroke="#fff" stroke-width="2.5" fill="none"/></svg></div>

  <div class="svc" style="left:110px">
    <div class="pic" style="background:linear-gradient(150deg,#8c7a66,#b5aea2)" role="img" aria-label="Concrete path beside a timber deck"></div>
    <div class="icon"><svg width="30" height="30" viewBox="0 0 30 30" fill="none" stroke="#fff" stroke-width="2"><rect x="4" y="4" width="22" height="22"/><path d="M4 15h22M15 4v22"/></svg></div>
    <h3>LOREM IPSUM DOLOR</h3>
    <p>Lorem ipsum dolor sit amet, consectetur adipiscing elit, sed do eiusmod tempor incididunt.</p>
    <span class="btn btn-outline">Learn More</span>
  </div>
  <div class="svc mid" style="left:450px">
    <div class="pic" style="background:linear-gradient(170deg,#6f8ab5,#4c5058 60%,#7a7a7a)" role="img" aria-label="Wide concrete driveway in front of a house"></div>
    <div class="icon"><svg width="30" height="30" viewBox="0 0 30 30" fill="none" stroke="#fff" stroke-width="2"><path d="M5 24h20M8 24V12l7-6 7 6v12"/></svg></div>
    <h3>LOREM IPSUM DOLOR</h3>
    <p>Lorem ipsum dolor sit amet, consectetur adipiscing elit, sed do eiusmod tempor incididunt.</p>
    <span class="btn btn-blue">Learn More</span>
  </div>
  <div class="svc" style="left:790px">
    <div class="pic" style="background:linear-gradient(150deg,#a7a49e,#6e6c68)" role="img" aria-label="Concrete garage floor"></div>
    <div class="icon"><svg width="30" height="30" viewBox="0 0 30 30" fill="none" stroke="#fff" stroke-width="2"><path d="M6 24 22 8M6 24h18"/></svg></div>
    <h3>LOREM IPSUM DOLOR</h3>
    <p>Lorem ipsum dolor sit amet, consectetur adipiscing elit, sed do eiusmod tempor incididunt.</p>
    <span class="btn btn-outline">Learn More</span>
  </div>
</section>

<!-- Benefits -->
<section class="abs benefits">
  <svg class="abs" style="left:0;top:0" width="1200" height="600" viewBox="0 0 1200 600">
    <path d="M0 0 L1200 40 L1200 600 L0 600Z" fill="#1f3f9f"/>
    <path d="M0 0 L1200 40 L1200 70 L0 20Z" fill="#162e7a" opacity=".6"/>
  </svg>
  <h2 class="heading">OUR <span style="color:#fff">BENEFITS</span></h2>
  <ul>
    <li>Lorem ipsum dolor sit amet, consectetur adipiscing elit, sed do eiusmod tempor incididunt ut labore et dolore magna aliqua. Ut enim ad minim veniam.</li>
    <li>Lorem ipsum dolor sit amet, consectetur adipiscing elit, sed do eiusmod tempor incididunt ut labore et dolore.</li>
    <li>Lorem ipsum dolor sit amet, consectetur adipiscing elit, sed do eiusmod tempor incididunt ut labore et dolore magna aliqua. Ut enim ad minim veniam.</li>
    <li>Lorem ipsum dolor sit amet, consectetur adipiscing elit, sed do eiusmod tempor incididunt ut labore et dolore.</li>
  </ul>
  <div class="actions"><span class="btn btn-dark">Learn More</span><span class="btn btn-white">&#9742; +61 400 000 123</span></div>
</section>
<div class="abs benefit-photo" role="img" aria-label="Smooth concrete courtyard surrounded by garden plants"></div>

<!-- Projects -->
<h2 class="abs heading projects-title">OUR <span>PROJECTS</span></h2>
<div class="abs proj" style="left:112px;top:2980px;width:480px;height:284px;background:linear-gradient(160deg,#4d6a3a,#a29d92 40%,#8a8780)" role="img" aria-label="Large exposed aggregate driveway"></div>
<div class="abs proj" style="left:608px;top:2980px;width:480px;height:284px;background:linear-gradient(170deg,#e2ddd3,#b6b1a7 55%,#9c988f)" role="img" aria-label="Concrete patio beside a verandah"></div>
<div class="abs proj" style="left:112px;top:3280px;width:312px;height:244px;background:linear-gradient(170deg,#6d8a5a,#8e8b84 50%,#6f6d69)" role="img" aria-label="Concrete path along a lawn"></div>
<div class="abs proj" style="left:440px;top:3280px;width:312px;height:244px;background:linear-gradient(170deg,#8aa3c4,#6c6f73 45%,#55565a)" role="img" aria-label="Dark concrete driveway on a sloped street"></div>
<div class="abs proj blue" style="left:768px;top:3280px;width:320px;height:244px;background:linear-gradient(170deg,#5b5348,#86827a 55%,#6b6862)" role="img" aria-label="Concrete steps with a stone retaining wall"></div>

<!-- Footer -->
<footer class="abs footer">
  <svg class="abs" style="left:0;top:0" width="1200" height="540" viewBox="0 0 1200 540">
    <path d="M0 150 C300 40 700 20 1200 60 L1200 540 L0 540Z" fill="#1f3f9f"/>
    <path d="M0 180 C300 70 700 50 1200 90 L1200 540 L0 540Z" fill="#2a2a2a"/>
  </svg>
  <div class="abs f-logo">TARVEN<span class="l2">GROUP</span></div>
  <div class="abs f-col" style="left:380px">
    <h4>NAVIGATION</h4>
    <ul><li>Home</li><li>About Us</li><li>Services</li><li>Projects</li><li>Contact Us</li></ul>
  </div>
  <div class="abs f-col" style="left:592px">
    <h4>QUICK LINKS</h4>
    <ul><li>News</li><li>Career</li><li>Privacy Police</li><li>Terms Of Use</li></ul>
  </div>
  <div class="abs f-col" style="left:820px">
    <h4>CONTACT US</h4>
    <div class="contact-row"><div class="ic"><svg width="18" height="18" viewBox="0 0 24 24"><path fill="#2a2a2a" d="M12 2a7 7 0 0 0-7 7c0 5 7 13 7 13s7-8 7-13a7 7 0 0 0-7-7zm0 9.5A2.5 2.5 0 1 1 12 6a2.5 2.5 0 0 1 0 5.5z"/></svg></div><div><b>LOCATIONS:</b><span>Adelaide, SA, Australia, South Australia</span></div></div>
    <div class="contact-row"><div class="ic"><svg width="18" height="18" viewBox="0 0 24 24"><path fill="#2a2a2a" d="M6.6 10.8a15.1 15.1 0 0 0 6.6 6.6l2.2-2.2c.3-.3.7-.4 1-.2 1.1.4 2.3.6 3.6.6.6 0 1 .4 1 1V20c0 .6-.4 1-1 1A17 17 0 0 1 3 4c0-.6.4-1 1-1h3.5c.6 0 1 .4 1 1 0 1.2.2 2.4.6 3.6.1.3 0 .7-.2 1z"/></svg></div><div><b>PHONE:</b><span>+61 400 000 123</span></div></div>
    <div class="contact-row"><div class="ic"><svg width="18" height="18" viewBox="0 0 24 24"><path fill="#2a2a2a" d="M3 5h18v14H3zm2 2v.5l7 5 7-5V7z"/></svg></div><div><b>EMAIL:</b><span>hello@tarvengroup.example</span></div></div>
  </div>
  <div class="abs f-bottom">© 2024 TARVEN GROUP &nbsp;|&nbsp; All Rights Reserved
    <div class="f-social"><i></i><i class="on"></i><i></i></div>
  </div>
</footer>

</body>
</html>
```